Funeral Comparison Website Needs Designer For WireFrame Mock Up (That we've already done)

This should be a pretty quick design project. It's a single page based on a wireframe mockup we did.
Our site (restfulchoices.net) helps people find and compare funeral homes and cemeteries. Our site hasn't been redesigned since we launched in 2008, so it is fairly dated, and we've seen new competitors pop-up in the past year so we need to come up with a fresh redeisgn. We need someone to take our mockup and work their magic with it. As I mentioned this is a single page based on our wireframe mockup.
Please see attached mockup and logo.
Look and feel
Each slider illustrates characteristics of the customer's brand and the style your logo design should communicate.

```html
<!DOCTYPE html>
<html lang="en">
<head>
<meta charset="utf-8">
<title>restfulchoices.net — Request Funeral Quotes</title>
<link rel="stylesheet" href="https://fonts.googleapis.com/css2?family=Mulish:wght@300;400;600&display=swap">
<style>
  :root {
    --bar-blue: #5a76a0;
    --phone-dark: #17384f;
    --social-tint: #c9d2ee;
    --title-blue: #1d7ba3;
    --leaf-green: #3f9a48;
    --or-green: #8dc500;
    --card-green-top: #9bcb00;
    --card-green-bottom: #6a962e;
    --card-blue-top: #82b6ec;
    --card-blue-bottom: #35679b;
    --card-taupe-top: #a39b9b;
    --card-taupe-bottom: #6c5a57;
    --resource-ink: #1b4e6e;
    --testimonial-head: #5b72a0;
    --body-ink: #4b5b68;
    --white: #ffffff;
  }
  * { box-sizing: border-box; margin: 0; padding: 0; }
  html, body { width: 1200px; height: 1000px; overflow: hidden; background: var(--white); }
  body { position: relative; font-family: "Mulish", "Helvetica Neue", Arial, sans-serif; }

  .top-bar { position: absolute; left: 0; top: 0; width: 1200px; height: 60px; background: var(--bar-blue); }
  .main-nav a { position: absolute; top: 20px; color: var(--white); font: 15px Arial, Helvetica, sans-serif; text-decoration: none; }
  .phone-icon { position: absolute; left: 821px; top: 16px; }
  .phone-number { position: absolute; left: 858px; top: 15px; color: var(--white); font-size: 22px; font-weight: 300; letter-spacing: .3px; }
  .social { position: absolute; top: 16px; width: 28px; height: 28px; border-radius: 50%; background: var(--social-tint); }

  .brand-dome { position: absolute; left: 440px; top: 18px; }
  .brand-name { position: absolute; left: 0; width: 1200px; top: 100px; text-align: center; color: var(--title-blue); font-size: 34px; font-weight: 600; }

  .page-title { position: absolute; left: 0; width: 1200px; top: 214px; text-align: center; color: var(--title-blue); font-size: 57px; font-weight: 300; letter-spacing: -.3px; }
  .page-subtitle { position: absolute; left: 0; width: 1200px; top: 285px; text-align: center; color: var(--leaf-green); font-size: 27px; font-weight: 400; }

  .hero-photo { position: absolute; left: 0; top: 330px; width: 1200px; height: 500px;
    background:
      radial-gradient(ellipse 180px 120px at 160px 110px, rgba(120,150,240,.8), transparent),
      radial-gradient(ellipse 220px 160px at 1000px 180px, rgba(110,140,230,.75), transparent),
      radial-gradient(ellipse 200px 140px at 500px 400px, rgba(130,160,240,.7), transparent),
      radial-gradient(ellipse 160px 200px at 1150px 120px, rgba(90,140,70,.7), transparent),
      radial-gradient(ellipse 200px 150px at 300px 250px, rgba(40,60,40,.6), transparent),
      linear-gradient(160deg, #5d78c8 0%, #3b4f6a 45%, #6c86d6 75%, #4f6b48 100%); }
  .title-panel { position: absolute; left: 120px; top: 330px; width: 960px; height: 24px; background: var(--white); border-radius: 0 0 6px 6px; }

  .choice { position: absolute; top: 420px; width: 300px; height: 220px; background: rgba(255,255,255,.4); border-radius: 5px; }
  .choice-face { position: absolute; left: 9px; top: 9px; width: 282px; height: 202px; border: 1px solid var(--white);
    display: flex; align-items: center; justify-content: center; text-align: center; padding: 0 24px;
    color: var(--white); font-size: 23px; font-weight: 300; line-height: 29px; }
  .choice-future .choice-face { background: linear-gradient(var(--card-green-top), var(--card-green-bottom)); }
  .choice-shortly .choice-face { background: linear-gradient(var(--card-blue-top), var(--card-blue-bottom)); }
  .choice-occurred .choice-face { background: linear-gradient(var(--card-taupe-top), var(--card-taupe-bottom)); }
  .or-badge { position: absolute; top: 490px; width: 80px; height: 80px; border-radius: 50%; background: var(--or-green);
    color: var(--white); display: flex; align-items: center; justify-content: center; gap: 6px; font-weight: 600; }
  .or-badge .paren { font-size: 36px; font-weight: 400; line-height: 1; margin-top: -4px; }
  .or-badge .word { font-size: 16px; font-family: Arial, sans-serif; font-weight: 700; }

  .resources-button { position: absolute; left: 450px; top: 690px; width: 300px; height: 50px; border-radius: 4px;
    background: linear-gradient(rgba(255,255,255,.85), rgba(255,255,255,.6));
    color: var(--resource-ink); font-size: 19px; font-weight: 400; text-align: center; line-height: 50px; }
  .resources-pointer { position: absolute; left: 585px; top: 740px; }

  .testimonial-panel { position: absolute; left: 120px; top: 790px; width: 960px; height: 260px; background: var(--white); border-radius: 6px 6px 0 0; }
  .testimonial-panel::before { content: ""; position: absolute; left: 10px; top: 10px; width: 940px; height: 32px; background: linear-gradient(#e4e8f0, #ffffff); }
  .testimonial-heading { position: absolute; left: 0; width: 960px; top: 28px; text-align: center; color: var(--testimonial-head); font-size: 29px; font-weight: 400; }
  .quote { position: absolute; top: 82px; width: 282px; color: var(--body-ink); font: italic 15px/24px Arial, Helvetica, sans-serif; }
</style>
</head>
<body>
  <header class="top-bar">
    <nav class="main-nav">
      <a href="#" style="left:130px">Menu Item</a>
      <a href="#" style="left:240px">Menu Item</a>
      <a href="#" style="left:350px">Menu Item</a>
    </nav>
    <svg class="phone-icon" width="28" height="28" viewBox="0 0 28 28" aria-hidden="true">
      <circle cx="14" cy="14" r="14" fill="var(--phone-dark)"/>
      <path d="M10 7c1-.6 2 1.8 2.4 2.8.3.8-1 1.3-.8 2.2.5 1.7 1.5 3 2.7 4 .7.4 1.4-.8 2.2-.5 1 .4 3.2 1.8 2.5 2.7-.9 1.2-2.5 1.6-4 .8-3-1.6-5.3-4.6-6-7.8-.3-1.7.1-3.4 1-4.2z" fill="#cfe0ee"/>
    </svg>
    <div class="phone-number">800.555.555</div>
    <span class="social" style="left:1010px"></span>
    <span class="social" style="left:1045px"></span>
  </header>

  <svg class="brand-dome" width="320" height="60" viewBox="0 0 320 60" aria-hidden="true">
    <defs><linearGradient id="domeShade" x1="0" y1="0" x2="0" y2="1"><stop offset="0" stop-color="#dfe3ea"/><stop offset=".6" stop-color="#fff"/></linearGradient></defs>
    <path d="M20 42 C 60 -10, 260 -10, 300 42 Z" fill="url(#domeShade)"/>
    <path d="M22 42 C 62 0, 258 0, 298 42" fill="none" stroke="#fff" stroke-width="3"/>
  </svg>
  <div class="brand-name">restfulchoices.net</div>

  <h1 class="page-title">Request Funeral Quotes</h1>
  <p class="page-subtitle">Free No Obligations Price &amp; Service Quotes</p>

  <div class="hero-photo" role="img" aria-label="Soft-focus photograph of small blue spring flowers among green leaves"></div>
  <div class="title-panel"></div>

  <a class="choice choice-future" href="#" style="left:120px"><span class="choice-face">I am planning for the long term future</span></a>
  <a class="choice choice-shortly" href="#" style="left:450px"><span class="choice-face">I am planning for a death that will occur shortly</span></a>
  <a class="choice choice-occurred" href="#" style="left:780px"><span class="choice-face">A death has just occurred</span></a>
  <div class="or-badge" style="left:395px"><span class="paren">(</span><span class="word">OR</span><span class="paren">)</span></div>
  <div class="or-badge" style="left:725px"><span class="paren">(</span><span class="word">OR</span><span class="paren">)</span></div>

  <div class="resources-button">Additional Resources</div>
  <svg class="resources-pointer" width="30" height="14" viewBox="0 0 30 14" aria-hidden="true">
    <path d="M0 0 H30 L15 13 Z" fill="rgba(255,255,255,.7)"/>
  </svg>

  <section class="testimonial-panel">
    <h2 class="testimonial-heading">Testimonials</h2>
    <p class="quote" style="left:22px">Lorem ipsum dolor sit amet, consectetur adipisicing elit, sed do eiusmod tempor incididunt ut labore et dolore magna aliqua. Ut enim ad minim veniam, quis nostrud exercitation ullamco laboris nisi ut aliquip ex ea commodo consequat.</p>
    <p class="quote" style="left:342px">Excepteur sint occaecat cupidatat non proident, sunt in culpa qui officia deserunt mollit anim id est laborum. Sed perspiciatis unde omnis iste natus error sit voluptatem accusantium doloremque laudantium, totam rem aperiam.</p>
    <p class="quote" style="left:662px">Sed ut perspiciatis unde omnis iste natus error sit voluptatem accusan laudantium, totam rem aperiam, eaque ipsa quae ab illo inventore veritatis et quasi architecto beatae vitae dicta sunt explicabo. Nemo enim ipsam voluptatem quia.</p>
  </section>
</body>
</html>
```